Zentro - revolutionary mobile payment

The app is a P2P money trasfert, without the using of credit card or bank circuits it can transfer electronic money from one person to another consumers simply and immediatelly.
You can use the color you want, but the message we need to transert to consumer is simplicity, safety and coolness.
In attach the logo of the company and the wireframe of thre page of the app.
The goal is to design the page of the app with a clear, simple and intuitive graphic.
Updates

I have upgrade the brief with important information and detail, many thanks

Target Market(s)

all the people

Industry/Entity Type

Credit Card

Requirements
Must have
• You have to design one icon for each button in the first page, (shop is: where to shop)
in the second one a new intuitive image (instead of the hand) that let the user to understand that with a simple swipe he can process the payment
Nice to have
• You can include or esxclude what you want or belive can improve user experience of the app
Should not have
• too much color, too much button or information

```html
<!DOCTYPE html>
<html lang="en">
<head>
<meta charset="utf-8">
<title>Zentro – app screens</title>
<link rel="stylesheet" href="https://fonts.googleapis.com/css2?family=Roboto:wght@400;500;700&display=swap">
<style>
:root{
  --bg:#ececec;
  --navy:#1b3366;
  --blue:#0a95e6;
  --wood:#c4622a;
  --wood-light:#dd8d4c;
  --wood-dark:#a84d1c;
  --white:#ffffff;
  --ink:#1d1d1d;
  --bar:#111111;
}
*{box-sizing:border-box;margin:0;padding:0}
html,body{width:1200px;height:816px;overflow:hidden;background:var(--bg);font-family:"Roboto",Arial,sans-serif}
.canvas{position:relative;width:1200px;height:816px}
.screen{position:absolute;top:178px;width:236px;height:418px;background:var(--white);overflow:hidden;border:2px solid var(--bar);box-shadow:0 8px 24px rgba(0,0,0,.12)}
.screen--welcome{left:289px}
.screen--home{left:698px}
.status-bar{height:19px;background:var(--bar);color:var(--white);font-size:8px;font-weight:700;display:flex;align-items:center;justify-content:space-between;padding:0 5px}
.status-bar .battery{display:inline-block;width:14px;height:6px;border:1px solid var(--white);margin-left:3px;vertical-align:middle;position:relative}
.status-bar .battery::after{content:"";position:absolute;left:0;top:0;width:3px;height:100%;background:var(--white)}
.wood{background:radial-gradient(ellipse at 50% 40%,var(--wood-light) 0%,var(--wood) 55%,var(--wood-dark) 100%)}
.welcome-hero{position:relative;height:256px}
.brand{position:absolute;left:47px;top:128px;display:flex;align-items:center;gap:8px}
.brand-dot{width:28px;height:28px;border-radius:50%;background:var(--navy)}
.brand-name{font-size:28px;font-weight:700;color:var(--navy);letter-spacing:.5px}
.btn{position:absolute;left:29px;width:182px;height:32px;border-radius:2px;color:var(--white);font-size:12px;display:flex;align-items:center;justify-content:center}
.btn--login{top:319px;background:var(--blue)}
.btn--register{top:368px;background:var(--navy)}
.app-header{height:37px;background:var(--navy);color:var(--white);display:flex;align-items:center;justify-content:space-between;padding:0 10px 0 12px;font-size:13px}
.profile{height:100px;display:flex;align-items:center;padding-left:15px;box-shadow:0 2px 3px rgba(0,0,0,.25);position:relative;z-index:1}
.avatar{width:70px;height:70px;border-radius:50%;background:linear-gradient(160deg,#b9b9b9,#6e6e6e);border:2px solid #e2e2e2;flex:none}
.profile-info{margin-left:12px;line-height:1.25}
.profile-name{color:var(--blue);font-size:13px}
.profile-address{color:var(--ink);font-size:7.5px}
.profile-email{color:var(--blue);font-size:7.5px}
.dashboard{position:relative;height:243px}
.tile{position:absolute;width:64px;height:64px;background:var(--white);border-radius:4px;box-shadow:0 2px 3px rgba(0,0,0,.3);display:flex;flex-direction:column;align-items:center;justify-content:center;gap:3px;font-size:9px;color:var(--ink)}
.tile svg{width:34px;height:32px}
.tile--pay{left:25px;top:30px}
.tile--ask{left:140px;top:30px}
.tile--account{left:25px;top:132px}
.tile--shop{left:140px;top:132px}
</style>
</head>
<body>
<div class="canvas">

  <section class="screen screen--welcome">
    <div class="status-bar"><span>●●●○○ ORBIT</span><span>4:21 PM</span><span>22%<i class="battery"></i></span></div>
    <div class="welcome-hero wood" role="img" aria-label="Wooden desk photo with banknotes, coins, a phone and a cup of coffee">
      <div class="brand"><span class="brand-dot"></span><span class="brand-name">Zentro</span></div>
    </div>
    <div class="btn btn--login">Login</div>
    <div class="btn btn--register">Registration</div>
  </section>

  <section class="screen screen--home">
    <div class="status-bar"><span>●●●○○ ORBIT</span><span>4:21 PM</span><span>22%<i class="battery"></i></span></div>
    <header class="app-header">
      <span>+39100200300</span>
      <svg width="20" height="20" viewBox="0 0 24 24" fill="none" stroke="#fff" stroke-width="1.5"><circle cx="12" cy="12" r="3.2"/><path d="M12 2.5l1.6 2.6 3-.8.8 3 2.6 1.6-1.3 2.8 1.3 2.8-2.6 1.6-.8 3-3-.8L12 21.5l-1.6-2.6-3 .8-.8-3L4 15.1l1.3-2.8L4 9.5l2.6-1.6.8-3 3 .8z"/></svg>
    </header>
    <div class="profile">
      <div class="avatar" role="img" aria-label="Profile photo of the user"></div>
      <div class="profile-info">
        <div class="profile-name">marco lenti</div>
        <div class="profile-address">Alder Bay, CA 95010-2231.</div>
        <div class="profile-email">marco lenti@mailbox.com</div>
      </div>
    </div>
    <div class="dashboard wood" role="img" aria-label="Wooden desk texture background">
      <div class="tile tile--pay">
        <svg viewBox="0 0 34 32"><path d="M2 16h8" stroke="#1b3366" stroke-width="3"/><path d="M9 11l6 5-6 5z" fill="#1b3366"/><rect x="19" y="2" width="13" height="28" rx="2" fill="none" stroke="#1b3366" stroke-width="2"/><text x="25.5" y="20" text-anchor="middle" font-size="12" font-weight="700" fill="#0a95e6" font-family="Roboto,Arial,sans-serif">$</text></svg>
        <span>Pay</span>
      </div>
      <div class="tile tile--ask">
        <svg viewBox="0 0 34 32"><path d="M17 3a13 11 0 1 1-7 20l-6 4 2-6A13 11 0 0 1 17 3z" fill="none" stroke="#1b3366" stroke-width="2"/><text x="17" y="19" text-anchor="middle" font-size="13" font-weight="700" fill="#0a95e6" font-family="Roboto,Arial,sans-serif">$</text></svg>
        <span>Ask</span>
      </div>
      <div class="tile tile--account">
        <svg viewBox="0 0 34 32"><path d="M5 8l18-5 1 5z" fill="#1b3366"/><rect x="3" y="8" width="28" height="22" rx="3" fill="#1b3366"/><circle cx="27" cy="19" r="2" fill="#0a95e6"/></svg>
        <span>Account</span>
      </div>
      <div class="tile tile--shop">
        <svg viewBox="0 0 34 32"><path d="M2 4h6l4 18h16" fill="none" stroke="#1b3366" stroke-width="2"/><path d="M10 9h22M11 13h19M12 17h16" stroke="#1b3366" stroke-width="2"/><circle cx="15" cy="27" r="2.5" fill="#0a95e6"/><circle cx="25" cy="27" r="2.5" fill="#0a95e6"/></svg>
        <span>Shop</span>
      </div>
    </div>
  </section>

</div>
</body>
</html>
```